Business card required for IT Consultancy Business - Tealbrook Consulting.
Company provides the whole nine yards of services across IT Architecture, design and execution.
Basically we provide consulting services to help businesses make sure their technology is enabling their business strategy.
Design for front and back required.
We would like the front of the card to inlcude:
Name
Title
Mobile number
email address
www.tbkc.com.au
Company logos attached.
Thank you
Industry/Entity Type
Business
Contact Information for Business Card
Name
Title
Mobile number
email address
www.tbkc.com.au
Look and feel
Each slider illustrates characteristics of the customer's brand and the style your logo design should communicate.

```html
<!DOCTYPE html>
<html lang="en">
<head>
<meta charset="utf-8">
<title>Tealbrook Consulting – Business Card</title>
<link rel="stylesheet" href="https://fonts.googleapis.com/css2?family=Arimo:wght@400;700&display=swap">
<style>
  :root {
    --brand-blue: #1573bd;
    --brand-orange: #f15a24;
    --card-white: #ffffff;
    --ink-grey: #4a4a4a;
    --backdrop: #2b2b2b;
  }
  * { box-sizing: border-box; margin: 0; padding: 0; }
  html, body { width: 1200px; height: 880px; overflow: hidden; }
  body {
    background: var(--backdrop);
    font-family: "Arimo", Arial, sans-serif;
    position: relative;
  }
  .card {
    position: absolute;
    width: 560px;
    height: 320px;
    border-radius: 22px;
    overflow: hidden;
    box-shadow: 0 14px 30px rgba(0,0,0,.45);
  }
  /* Back side */
  .card-back {
    left: 40px; top: 90px;
    background: var(--brand-blue);
    display: flex; flex-direction: column; align-items: center; justify-content: center;
    color: var(--card-white);
  }
  .back-mark { display: flex; align-items: center; gap: 14px; }
  .back-mark .dot {
    width: 34px; height: 34px; border-radius: 50%; background: var(--card-white);
  }
  .back-mark .wordmark { font-size: 40px; font-weight: 700; letter-spacing: .5px; }
  .back-url { margin-top: 58px; font-size: 15px; letter-spacing: 1.5px; }

  /* Front side */
  .card-front {
    left: 600px; top: 470px;
    background: var(--card-white);
  }
  .card-front .swoosh { position: absolute; inset: 0; }
  .front-mark {
    position: absolute; right: 40px; top: 48px;
    display: flex; align-items: center; gap: 10px;
    color: var(--brand-blue);
  }
  .front-mark .dot {
    width: 26px; height: 26px; border-radius: 50%; background: var(--brand-blue);
  }
  .front-mark .wordmark { font-size: 30px; font-weight: 700; }
  .person { position: absolute; left: 250px; top: 168px; }
  .person .name { color: var(--brand-blue); font-weight: 700; font-size: 19px; letter-spacing: .3px; }
  .person .title { color: var(--brand-orange); font-size: 14px; margin-top: 2px; }
  .rule {
    position: absolute; left: 250px; right: 34px; top: 214px;
    height: 1px; background: var(--brand-orange);
  }
  .contacts {
    position: absolute; left: 250px; top: 226px; list-style: none;
    font-size: 13px; color: var(--ink-grey);
  }
  .contacts li { display: flex; align-items: center; gap: 8px; height: 22px; }
  .contacts .icon {
    width: 17px; height: 17px; border: 1.5px solid var(--brand-orange); border-radius: 50%;
    display: flex; align-items: center; justify-content: center;
  }
  .address {
    position: absolute; right: 34px; top: 146px;
    text-align: right; font-size: 13px; line-height: 18px; color: var(--ink-grey);
    font-style: normal;
  }
</style>
</head>
<body>

<section class="card card-back" aria-label="Card back">
  <div class="back-mark">
    <span class="dot"></span>
    <span class="wordmark">Tealbrook Consulting</span>
  </div>
  <p class="back-url">www.tbkc.com.au</p>
</section>

<section class="card card-front" aria-label="Card front">
  <svg class="swoosh" viewBox="0 0 560 320" preserveAspectRatio="none" aria-hidden="true">
    <path d="M0 0 H125 C55 120 95 255 225 320 H0 Z" fill="var(--brand-blue)"/>
    <path d="M140 0 H172 C118 80 112 170 150 232 C104 172 102 82 140 0 Z" fill="var(--brand-orange)"/>
  </svg>

  <div class="front-mark">
    <span class="dot"></span>
    <span class="wordmark">Tealbrook Consulting</span>
  </div>

  <div class="person">
    <p class="name">NORA PELL</p>
    <p class="title">Managing Director</p>
  </div>

  <address class="address">
    PO BOX 418<br>
    Harbour Lane<br>
    3rd street Perth, AUS
  </address>

  <div class="rule"></div>

  <ul class="contacts">
    <li>
      <span class="icon"><svg width="8" height="11" viewBox="0 0 8 11"><rect x="1" y="0.5" width="6" height="10" rx="1" fill="none" stroke="var(--brand-blue)" stroke-width="1.2"/></svg></span>
      (01) 5550 1427
    </li>
    <li>
      <span class="icon"><svg width="10" height="8" viewBox="0 0 10 8"><rect x="0.5" y="0.5" width="9" height="7" fill="var(--brand-blue)"/><path d="M0.5 0.5 L5 4.5 L9.5 0.5" fill="none" stroke="#fff" stroke-width="1"/></svg></span>
      hello@tbkc.com.au
    </li>
    <li>
      <span class="icon"><svg width="10" height="10" viewBox="0 0 10 10"><circle cx="5" cy="5" r="4.5" fill="var(--brand-blue)"/><path d="M0.5 5 H9.5 M5 0.5 C2.5 3 2.5 7 5 9.5 M5 0.5 C7.5 3 7.5 7 5 9.5" fill="none" stroke="#fff" stroke-width=".8"/></svg></span>
      www.tbkc.com.au
    </li>
  </ul>
</section>

</body>
</html>
```